Coffee and hot drinks advert on A-Board

Creative eye catching design to advertise coffee and hot drinks on an A-Board.

To use images and modern design to reflect the quality and almost specialist coffee house style drinks on offer.
We use organic milk and have had our own 'Millbrook Restaurant' coffee beans roasted to produce the perfect coffee.
We also use only the best hot chocolate and fresh cream to serve quality drinks.
All staff are barista trained.

Target Market(s)

Passing trade and coffee lovers for takeaway drinks

Industry/Entity Type

Coffee Shop

Font styles to use
Serif

Requirements
Must have
• Bold creative modern look.
• Independent coffee shop style look
• Mention we use 'Heron Organic milk'
• We use our own roasted special blend of coffee
• speciality hot chocolate
Nice to have
• modern approach
• eye catching
Should not have
• complicated
• difficult to read
• old fashioned

```html
<!DOCTYPE html>
<html lang="en">
<head>
<meta charset="utf-8">
<title>Millbrook Restaurant – Coffee A-Board</title>
<link rel="stylesheet" href="https://fonts.googleapis.com/css2?family=Pacifico&family=Sofia+Sans+Extra+Condensed:wght@300;400&display=swap">
<style>
  :root {
    --backdrop: #ececec;
    --teal-light: #5fc4d1;
    --teal-mid: #55b2bd;
    --teal-dark: #48939b;
    --ink: #ffffff;
    --photo-light: #e9e2d3;
    --photo-warm: #c99a5c;
  }
  * { margin: 0; padding: 0; box-sizing: border-box; }
  html, body {
    width: 1200px;
    height: 1200px;
    overflow: hidden;
    background: var(--backdrop);
  }
  .board {
    position: absolute;
    left: 176px;
    top: 0;
    width: 848px;
    height: 1200px;
    background: radial-gradient(ellipse 62% 48% at 50% 55%, var(--teal-light) 0%, var(--teal-mid) 62%, var(--teal-dark) 100%);
    color: var(--ink);
    text-align: center;
  }
  .brand {
    position: absolute;
    top: 82px;
    left: 0;
    width: 100%;
    padding-left: 10px;
    font-family: "Pacifico", cursive;
    font-weight: 400;
    font-size: 70px;
    line-height: 1.2;
    letter-spacing: -1px;
    white-space: nowrap;
  }
  .blend-line {
    position: absolute;
    top: 214px;
    left: 92px;
    width: 672px;
    font-family: "Sofia Sans Extra Condensed", sans-serif;
    font-weight: 300;
    font-size: 53px;
    line-height: 1.1;
    text-align: right;
    white-space: nowrap;
  }
  .rule {
    position: absolute;
    left: 92px;
    width: 672px;
    height: 2px;
    background: var(--ink);
  }
  .rule--top { top: 282px; }
  .rule--bottom { top: 381px; }
  .milk-line {
    position: absolute;
    top: 292px;
    left: 92px;
    width: 672px;
    display: flex;
    align-items: baseline;
    justify-content: space-between;
    white-space: nowrap;
  }
  .milk-line__with {
    font-family: "Pacifico", cursive;
    font-size: 32px;
    line-height: 1;
  }
  .milk-line__name {
    font-family: "Sofia Sans Extra Condensed", sans-serif;
    font-weight: 300;
    font-size: 82px;
    line-height: 1;
    letter-spacing: -1px;
  }
  .coffee-photo {
    position: absolute;
    left: 182px;
    top: 512px;
    width: 476px;
    height: 370px;
    border-radius: 24px;
    background: radial-gradient(ellipse 60% 60% at 50% 45%, var(--photo-warm) 0%, var(--photo-light) 70%, var(--teal-light) 100%);
  }
  .hot-chocolate {
    position: absolute;
    top: 1008px;
    left: 0;
    width: 100%;
    padding-right: 40px;
    font-family: "Pacifico", cursive;
    font-size: 33px;
    line-height: 1.4;
    letter-spacing: -0.5px;
    white-space: nowrap;
  }
  .takeaway {
    position: absolute;
    top: 1072px;
    left: 0;
    width: 100%;
    padding-right: 40px;
    font-family: "Sofia Sans Extra Condensed", sans-serif;
    font-weight: 300;
    font-size: 58px;
    line-height: 1.1;
    white-space: nowrap;
  }
</style>
</head>
<body>
  <main class="board">
    <h1 class="brand">Millbrook Restaurant</h1>
    <p class="blend-line">We use our own roasted special blend of coffee</p>
    <div class="rule rule--top"></div>
    <p class="milk-line">
      <span class="milk-line__with">with</span>
      <span class="milk-line__name">HERON DIARY ORGANIC MILK</span>
    </p>
    <div class="rule rule--bottom"></div>
    <div class="coffee-photo" role="img" aria-label="Photograph of a latte with leaf latte art in a white cup on a saucer"></div>
    <p class="hot-chocolate">~ Speciality hot chocolate ~</p>
    <p class="takeaway">ORDER YOUR TAKEAWAY HERE</p>
  </main>
</body>
</html>
```